Verdant Holdings Scholarship

Looking to make an attractive scholarship description graphic for my website. Please use the text on the word doc and integrate the two graphics into the layout. Here's what I am looking to replace with the winning design: https://qvandrellc.com/scholarship-contest/

Thank you

```html
<!DOCTYPE html>
<html lang="en">
<head>
<meta charset="utf-8">
<title>Verdant Holdings Scholarship</title>
<link rel="stylesheet" href="https://fonts.googleapis.com/css2?family=Roboto:wght@400;500;700&display=swap">
<style>
  :root {
    --paper: #ececec;
    --gold: #d6b543;
    --purple: #5b2e84;
    --plum: #33194f;
    --night: #2d1a48;
    --ink: #3a1e5c;
    --white: #ffffff;
  }
  * { box-sizing: border-box; margin: 0; padding: 0; }
  html, body { width: 927px; height: 1200px; overflow: hidden; }
  body { font-family: "Roboto", Arial, sans-serif; background: var(--paper); }
  .flyer { position: relative; width: 927px; height: 1200px; overflow: hidden; background: var(--paper); }

  .hero-photo {
    position: absolute; left: 338px; top: 0; width: 589px; height: 467px;
    background: linear-gradient(180deg, #f2f2f2 0%, #dcdcdc 40%, #2a2a2a 72%, #151515 100%);
  }

  .brand { position: absolute; left: 66px; top: 150px; display: flex; align-items: center; gap: 14px; }
  .brand-mark { width: 22px; height: 22px; background: var(--gold); }
  .brand-name { font-size: 34px; font-weight: 500; color: var(--purple); line-height: 1.1; }
  .brand-url { position: absolute; left: 102px; top: 195px; font-size: 9px; letter-spacing: .5px; color: var(--purple); }

  .purpose-kicker { position: absolute; left: 88px; top: 374px; font-size: 20px; font-weight: 400; color: var(--purple); }
  .purpose-title { position: absolute; left: 87px; top: 408px; font-size: 37px; font-weight: 400; line-height: 1.1; color: var(--purple); }

  .gold-band { position: absolute; left: 0; top: 467px; width: 927px; height: 87px; background: var(--gold); }
  .white-field { position: absolute; left: 0; top: 554px; width: 927px; height: 378px; background: var(--white); }

  .purpose-panel { position: absolute; left: 65px; top: 467px; width: 387px; height: 285px; background: var(--purple); padding: 15px 18px 0 18px; }
  .purpose-item { display: flex; gap: 11px; color: var(--white); font-size: 19px; line-height: 1.3; padding: 0 0 13px; border-bottom: 1px solid rgba(255,255,255,.18); margin-bottom: 12px; }
  .purpose-item:last-child { border-bottom: 0; }
  .dot { flex: none; width: 15px; height: 15px; border-radius: 50%; background: var(--gold); margin-top: 5px; }

  .application-panel { position: absolute; left: 65px; top: 752px; width: 387px; height: 180px; background: var(--plum); }
  .application-title { position: absolute; left: 18px; top: 16px; font-size: 33px; font-weight: 400; line-height: 1.1; color: var(--white); }
  .application-icon { position: absolute; left: 18px; top: 64px; }
  .application-text { position: absolute; left: 148px; top: 64px; width: 205px; font-size: 15px; line-height: 1.3; color: var(--white); }

  .eligibility-head { position: absolute; left: 470px; top: 484px; display: flex; align-items: center; gap: 20px; }
  .eligibility-head h2 { font-size: 17.5px; font-weight: 700; color: var(--ink); line-height: 1.35; width: 320px; }

  .requirements { position: absolute; left: 472px; top: 580px; width: 430px; list-style: none; }
  .requirement { display: flex; gap: 22px; font-size: 19px; line-height: 1.35; color: var(--ink); margin-bottom: 24px; }
  .requirement span { width: 305px; }
  .requirement svg { flex: none; }

  .footer { position: absolute; left: 0; top: 932px; width: 927px; height: 268px; background: var(--night); }
  .email-pill { position: absolute; left: 71px; top: 19px; width: 783px; height: 44px; border-radius: 22px; background: var(--gold); display: flex; align-items: center; padding-left: 50px; font-size: 22px; color: var(--night); }
  .email-pill svg { margin-left: 16px; }
  .package-label { position: absolute; left: 118px; top: 82px; font-size: 19.5px; color: var(--white); }
</style>
</head>
<body>
<main class="flyer">
  <div class="hero-photo" role="img" aria-label="Photo of three smiling graduates in caps and gowns holding diplomas tied with red ribbon"></div>

  <div class="brand">
    <span class="brand-mark"></span>
    <span class="brand-name">Verdant Holdings</span>
  </div>
  <div class="brand-url">WWW.QVANDRELLC.COM</div>

  <p class="purpose-kicker">Purpose of this</p>
  <h1 class="purpose-title">Scholarship:</h1>

  <div class="gold-band"></div>
  <div class="white-field"></div>

  <section class="purpose-panel">
    <div class="purpose-item"><span class="dot"></span><span>To increase trade school, college, and university opportunities of high school seniors</span></div>
    <div class="purpose-item"><span class="dot"></span><span>To encourage high academic achievement in our youth</span></div>
    <div class="purpose-item"><span class="dot"></span><span>To reward hard-working high school seniors and assist in collegiate expenses</span></div>
  </section>

  <section class="application-panel">
    <h2 class="application-title">Application:</h2>
    <svg class="application-icon" width="112" height="100" viewBox="0 0 118 100" fill="none" stroke="#d6b543" stroke-width="3">
      <rect x="6" y="22" width="86" height="58" rx="4"/>
      <rect x="20" y="32" width="86" height="58" rx="4" fill="#33194f"/>
      <circle cx="63" cy="61" r="14"/>
      <path d="M59 54 L70 61 L59 68 Z"/>
      <path d="M72 14 L92 6 L112 14 L92 22 Z"/>
      <path d="M100 18 V30"/>
    </svg>
    <p class="application-text">The application can be submitted via upload on this website, mail (see mailing address below), or scan &amp; email.</p>
  </section>

  <div class="eligibility-head">
    <svg width="48" height="50" viewBox="0 0 46 48" fill="none" stroke="#3a1e5c" stroke-width="2.2">
      <circle cx="23" cy="28" r="17"/>
      <ellipse cx="23" cy="28" rx="8" ry="17"/>
      <path d="M6 28 H40 M9 19 H37 M9 37 H37"/>
      <path d="M10 9 L23 3 L36 9 L23 15 Z" fill="#3a1e5c"/>
    </svg>
    <h2>Eligibility and Requirements at the time of submission for this scholarship:</h2>
  </div>

  <ul class="requirements">
    <li class="requirement">
      <svg width="42" height="46" viewBox="0 0 40 44" fill="none" stroke="#3a1e5c" stroke-width="2"><rect x="14" y="10" width="22" height="16"/><circle cx="12" cy="18" r="5"/><path d="M2 40 C2 28 22 28 22 40 Z M4 6 L12 2 L20 6 L12 10 Z"/></svg>
      <span>Applicant must be an enrolled high school student in his/her senior year</span>
    </li>
    <li class="requirement">
      <svg width="42" height="46" viewBox="0 0 40 44" fill="none" stroke="#3a1e5c" stroke-width="2"><circle cx="20" cy="8" r="4"/><path d="M20 12 V26 M10 12 L20 18 L30 12 M14 34 H26 V28 H14 Z M8 40 H32 V34 H8 Z"/></svg>
      <span>Applicant must be in good standing with their high school</span>
    </li>
    <li class="requirement">
      <svg width="42" height="46" viewBox="0 0 40 44" fill="none" stroke="#3a1e5c" stroke-width="2"><rect x="4" y="6" width="30" height="34" rx="2"/><path d="M10 16 H28 M10 22 H28 M10 28 H22 M10 34 H28"/></svg>
      <span>Applicant must have a cumulative grade point average of at least 2.5 on a 4.0 scale</span>
    </li>
    <li class="requirement">
      <svg width="42" height="46" viewBox="0 0 40 44" fill="none" stroke="#3a1e5c" stroke-width="2"><path d="M3 8 L6 11 L11 4 M3 20 L6 23 L11 16 M3 32 L6 35 L11 28"/><circle cx="26" cy="10" r="5"/><path d="M18 40 V22 H34 V40"/></svg>
      <span>Applicant must be accepted to a 4-year accredited college, university, trade school or community college</span>
    </li>
  </ul>

  <footer class="footer">
    <div class="email-pill">Email address: dana.reyes@qvandrellc.com.
      <svg width="24" height="26" viewBox="0 0 24 26"><path d="M2 2 L22 12 L13 14 L9 24 Z" fill="#2d1a48"/></svg>
    </div>
    <p class="package-label">The Application package must include:</p>
  </footer>
</main>
</body>
</html>
```